Luxury Business Card Design for Carriage Velmont

I need a high-end, luxury business card design for my premium limo service, Carriage Velmont. The card should reflect elegance and exclusivity, using a black and gold color scheme with a minimalist and sophisticated layout. The design should include:

Target Market(s)

High-end clients, corporate executives, luxury travelers, VIPs, and celebrities looking for premium limousine and chauffeur services

Industry/Entity Type

Limo

Contact Information for Business Card

Cluttered design—should be sleek & minimal

Font styles to use
Other font styles liked:
• CINZEL DECORATIVE

Requirements
Must have
• 📞 416-391-CARS (416-391-2277) 📞 Toll-Free: 1 (888) 604-CARS (2277) Email: book@carriage-velmont.com
Nice to have
• QR Code , I need a high-end, luxury business card design for my premium limo service, Carriage Velmont. The card should reflect elegance and exclusivity, using a black and gold color scheme with a minimalist and sophisticated layout. It should align with the branding, luxury feel, and premium aesthetics seen on our website www.carriage-velmont.com.

```html
<!DOCTYPE html>
<html lang="en">
<head>
<meta charset="utf-8">
<title>Carriage Velmont – Business Card</title>
<link href="https://fonts.googleapis.com/css2?family=Cinzel:wght@600&family=Montserrat:wght@400&display=swap" rel="stylesheet">
<style>
:root{
  --backdrop:#2f2f31;
  --card:#1b1b1c;
  --card-edge:#111112;
  --gold:#c9a24a;
  --gold-line:#b8923c;
  --red:#a3161c;
  --ink:#d9d9d9;
  --emboss:#2a2a2b;
}
*{margin:0;padding:0;box-sizing:border-box}
html,body{width:1200px;height:799px;overflow:hidden;background:var(--backdrop)}
.canvas{position:relative;width:1200px;height:799px;display:flex;align-items:center;justify-content:center;gap:50px}
.card{position:relative;width:540px;height:309px;background:var(--card);border:1px solid var(--card-edge);overflow:hidden}
.brand{font-family:"Cinzel",serif;font-weight:600;color:var(--gold);letter-spacing:1px;white-space:nowrap}
/* back side */
.card-back{display:flex;align-items:center;justify-content:center}
.card-back .brand{font-size:40px;color:#8c8c8c}
/* front side */
.crest-watermark{position:absolute;left:20px;top:10px;width:250px;height:290px;border-radius:40% 40% 10% 10%;background:radial-gradient(ellipse at center,var(--emboss) 0%,var(--card) 75%)}
.holder{position:absolute;left:36px;top:78px}
.holder-name{font-family:"Cinzel",serif;font-weight:600;font-size:21px;color:var(--gold);letter-spacing:1px;white-space:nowrap}
.holder-title{font-family:"Montserrat",sans-serif;font-size:12px;color:var(--red);margin-top:4px}
.divider{position:absolute;left:36px;right:28px;top:138px;height:1px;background:var(--gold-line)}
.contacts{position:absolute;left:36px;top:156px;list-style:none;font-family:"Montserrat",sans-serif;font-size:11.5px;color:var(--ink);line-height:21px}
.contacts li{display:flex;align-items:center;gap:9px}
.contacts svg{width:10px;height:10px;flex:none}
.logo-block{position:absolute;right:32px;top:40px;display:flex;flex-direction:column;align-items:center;gap:8px}
.logo-dot{width:26px;height:26px;border-radius:50%;background:var(--red)}
.logo-block .brand{font-size:20px}
.address{position:absolute;right:32px;bottom:26px;text-align:right;font-family:"Montserrat",sans-serif;font-size:12px;color:var(--ink);line-height:19px;font-style:normal}
</style>
</head>
<body>
<main class="canvas">
  <section class="card card-back" aria-label="Card back">
    <span class="brand">Carriage Velmont</span>
  </section>

  <section class="card card-front" aria-label="Card front">
    <div class="crest-watermark" role="img" aria-label="Faint embossed crest decoration"></div>

    <div class="holder">
      <p class="holder-name">Adrian Kessler</p>
      <p class="holder-title">Founder &amp; CEO</p>
    </div>

    <div class="logo-block">
      <span class="logo-dot"></span>
      <span class="brand">Carriage Velmont</span>
    </div>

    <div class="divider"></div>

    <ul class="contacts">
      <li><svg viewBox="0 0 10 10"><path d="M2 1l2 2-1 1.2c.6 1.2 1.6 2.2 2.8 2.8L7 6l2 2-1.3 1.3C4.5 9 1 5.5.7 2.3z" fill="var(--gold)"/></svg>416-391-CARS (416-391-2277)</li>
      <li><svg viewBox="0 0 10 10"><path d="M2 1l2 2-1 1.2c.6 1.2 1.6 2.2 2.8 2.8L7 6l2 2-1.3 1.3C4.5 9 1 5.5.7 2.3z" fill="var(--gold)"/></svg>Toll-Free: 1 (888) 604-CARS (2277)</li>
      <li><svg viewBox="0 0 10 10"><rect x="0.5" y="2" width="9" height="6.5" fill="var(--gold)"/><path d="M0.5 2l4.5 3.5L9.5 2" stroke="var(--card)" stroke-width="0.9" fill="none"/></svg>book@carriage-velmont.com</li>
      <li><svg viewBox="0 0 10 10"><circle cx="5" cy="5" r="4.2" fill="none" stroke="var(--gold)" stroke-width="1.2"/><path d="M1 5h8M5 1c-2 2.5-2 5.5 0 8M5 1c2 2.5 2 5.5 0 8" stroke="var(--gold)" stroke-width="0.8" fill="none"/></svg>carriage-velmont.com</li>
    </ul>

    <address class="address">
      Carriage Velmont<br>
      48 Harrow Lane<br>
      Velmont Tower, Suite 1200<br>
      Lakeview, ON L4R 2K8
    </address>
  </section>
</main>
</body>
</html>
```